Innovative Beverage Company needs a Packaging Design/Line Extension

We need a packaging design for a line extension for a new flavour of our beverage line called Vexa. Vexa is a 7% alcohol by volume "cooler" sold in aluminium cans. Its packaging is known for is bright colours and graphic design.

We are looking for a design that will "fit" with our existing product line. To "fit" the design will need to be somewhat different to the current products, but also complimentary in terms of design and chosen colours.

Attached are the current designs that we use, and the die-line.

Target Market(s)

The target demographic are women from 18 to 30.

Industry/Entity Type

It Company

Requirements
Must have
• We are looking for a design that will "fit" with our existing product line. To "fit" the design will need to be somewhat different to the current products, but also complimentary in terms of design and chosen colours.

```html
<!DOCTYPE html>
<html lang="fr">
<head>
<meta charset="utf-8">
<title>Vexa – Melon d'eau + Guarana</title>
<link rel="stylesheet" href="https://fonts.googleapis.com/css2?family=Ubuntu:wght@400;500;700&display=swap">
<style>
  :root {
    --royal-blue: #2a35b8;
    --sky-blue: #6cb4ee;
    --splash-red: #e8322f;
    --coral-red: #ee6a66;
    --label-white: #f7f7f7;
    --ink-grey: #3b3b3b;
    --page-bg: #ffffff;
  }
  * { margin: 0; padding: 0; box-sizing: border-box; }
  html, body {
    width: 689px;
    height: 1200px;
    overflow: hidden;
    background: var(--page-bg);
    font-family: "Ubuntu", sans-serif;
  }
  .can-label {
    position: relative;
    width: 689px;
    height: 1200px;
    overflow: hidden;
    background: var(--label-white);
  }
  .label-art {
    position: absolute;
    inset: 0;
    width: 689px;
    height: 1200px;
  }
  .product-info {
    position: absolute;
    left: 110px;
    top: 540px;
    color: var(--ink-grey);
  }
  .brand-name {
    font-weight: 500;
    font-size: 150px;
    line-height: 1;
    letter-spacing: 4px;
    color: var(--ink-grey);
  }
  .flavour-name {
    margin-top: 22px;
    margin-left: 8px;
    font-weight: 500;
    font-size: 44px;
    line-height: 1;
    color: var(--splash-red);
  }
  .flavour-boost {
    display: inline-block;
    margin-top: 12px;
    margin-left: 8px;
    padding: 4px 14px 3px;
    border-radius: 6px;
    background: var(--coral-red);
    color: var(--label-white);
    font-weight: 500;
    font-size: 24px;
    letter-spacing: 1px;
    line-height: 1.2;
  }
  .alcohol-content {
    margin-top: 10px;
    margin-left: 8px;
    font-weight: 400;
    font-size: 46px;
    line-height: 1.1;
    color: var(--ink-grey);
  }
  .legal-line {
    position: absolute;
    left: 0;
    right: 0;
    top: 1120px;
    text-align: center;
    color: var(--label-white);
    font-weight: 500;
    font-size: 28px;
    letter-spacing: 1px;
  }
</style>
</head>
<body>
  <main class="can-label">
    <svg class="label-art" viewBox="0 0 689 1200" xmlns="http://www.w3.org/2000/svg">
      <defs>
        <linearGradient id="top-splash-tone" x1="0" y1="0" x2="1" y2="1">
          <stop offset="0" stop-color="#5a6fd6"/>
          <stop offset="0.35" stop-color="#2a35b8"/>
          <stop offset="0.65" stop-color="#6cb4ee"/>
          <stop offset="1" stop-color="#e8322f"/>
        </linearGradient>
        <linearGradient id="bottom-splash-tone" x1="0" y1="0" x2="1" y2="1">
          <stop offset="0" stop-color="#e8322f"/>
          <stop offset="0.4" stop-color="#3c4fd0"/>
          <stop offset="0.75" stop-color="#2a35b8"/>
          <stop offset="1" stop-color="#e8322f"/>
        </linearGradient>
      </defs>
      <g role="img" aria-label="Éclaboussures de peinture bleues, bleu ciel et rouges">
        <rect class="top-splash" x="0" y="0" width="689" height="560" fill="url(#top-splash-tone)"/>
      </g>
      <g role="img" aria-label="Éclaboussures de peinture rouges et bleues">
        <rect class="bottom-splash" x="0" y="840" width="689" height="360" fill="url(#bottom-splash-tone)"/>
      </g>
      <path class="white-band" fill="var(--label-white)"
        d="M0 520 C 90 470, 170 540, 260 500 S 430 420, 520 470 S 640 430, 689 400
           L 689 900 C 620 880, 560 940, 470 915 S 320 870, 230 925 S 80 900, 0 945 Z"/>
    </svg>

    <section class="product-info">
      <h1 class="brand-name">Vexa</h1>
      <p class="flavour-name">Melon d’eau</p>
      <span class="flavour-boost">+ GUARANA</span>
      <p class="alcohol-content">7 % alc./vol.</p>
    </section>

    <p class="legal-line">BOISSON ALCOOLISÉE ALTERNATIVE &nbsp; 473 mL</p>
  </main>
</body>
</html>
```